Re-design of Business Card

We require a design for our business card.

Korrim is a supplier of industrial packaging specializing in plastic products. We are undergoing a rebranding to appear more corporate. We have changed our company name to korrim and have a new logo.

I have uploaded our old card design with the previous company name.
Don't copy the current design. We are looking for a new design.

Industry/Entity Type

Manufacturing

Contact Information for Business Card

please don't copy the current design. we are looking for a new design.

Font styles to use
Sans Serif

Colors

Designer to choose colors to be used in the design.

Requirements
Must have
• clean and easy to read.

```html
<!DOCTYPE html>
<html lang="en">
<head>
<meta charset="utf-8">
<title>Korrim Business Cards</title>
<link href="https://fonts.googleapis.com/css2?family=Montserrat:wght@400;600;700&display=swap" rel="stylesheet">
<style>
:root{
  --orange:#f47b20;
  --navy:#160a5a;
  --white:#ffffff;
  --page:#ffffff;
  --rule:#555555;
}
*{box-sizing:border-box;margin:0;padding:0}
html,body{width:1200px;height:1000px;overflow:hidden;background:var(--page);font-family:"Montserrat",Arial,sans-serif}
.card{position:absolute;width:542px;height:331px;border:1px solid var(--rule);background:var(--white);overflow:hidden}
.card > *{position:absolute}
.front-light{left:36px;top:107px}
.front-dark{left:620px;top:107px}
.back-light{left:38px;top:557px}
.back-dark{left:622px;top:557px;background:var(--navy);border-color:var(--navy)}
.brand-band{left:0;top:0;width:100%;height:168px;background:var(--navy)}
.brand-name{color:var(--orange);font-weight:700;letter-spacing:2px;line-height:1;white-space:nowrap}
.brand-lg{font-size:76px;left:0;width:100%;text-align:center;top:60px}
.brand-sm{font-size:34px;top:24px;width:148px;text-align:center}
.person-name{left:28px;top:218px;font-size:22px;font-weight:600;color:var(--navy)}
.person-role{left:28px;top:243px;font-size:14.5px;color:var(--navy)}
.row{display:flex;align-items:center;gap:6px;font-size:16px;color:var(--navy);white-space:nowrap}
.row svg{width:17px;height:17px;flex:none}
.divider{left:279px;top:200px;width:1px;height:105px;background:var(--orange)}
.address{left:308px;top:200px;display:flex;gap:8px;font-size:16.5px;color:var(--navy);line-height:20.5px}
.address svg{width:17px;height:17px;flex:none;margin-top:2px}
.badge{left:20px;width:84px;height:84px;border-radius:50%;border:6px solid var(--orange)}
.service-list{top:17px;list-style:none;font-size:14.5px;line-height:17px;color:var(--navy)}
.back-dark .service-list{color:var(--white)}
.service-list .group{color:var(--orange);font-weight:700;padding-left:14px;position:relative}
.service-list .group::before{content:"";position:absolute;left:0;top:4px;border-left:8px solid var(--navy);border-top:4.5px solid transparent;border-bottom:4.5px solid transparent}
.back-dark .service-list .group::before{border-left-color:var(--white)}
.service-list .item{padding-left:29px;position:relative}
.service-list .item::before{content:"";position:absolute;left:15px;top:6px;width:6px;height:6px;border-radius:50%;background:var(--orange)}
.map-area{width:185px;height:150px;border-radius:18px;background:linear-gradient(160deg,#f6923f,var(--orange))}
.hotline{font-size:21px;font-weight:700;color:var(--navy);width:182px;text-align:center;top:289px}
.back-dark .hotline{color:var(--white)}
.hairline{left:130px;width:182px;height:1px;background:var(--orange)}
</style>
</head>
<body>
<svg width="0" height="0" style="position:absolute" aria-hidden="true">
  <defs>
    <symbol id="ico-phone" viewBox="0 0 20 20"><circle cx="10" cy="10" r="10" fill="#f47b20"/><path d="M6.5 5h2l1 3-1.3 1a6 6 0 0 0 2.8 2.8l1-1.3 3 1v2a1.5 1.5 0 0 1-1.6 1.5A9 9 0 0 1 5 6.6 1.5 1.5 0 0 1 6.5 5z" fill="#fff"/></symbol>
    <symbol id="ico-mail" viewBox="0 0 20 20"><circle cx="10" cy="10" r="10" fill="#f47b20"/><rect x="5" y="6.5" width="10" height="7" fill="none" stroke="#fff" stroke-width="1.4"/><path d="M5 6.5l5 4 5-4" fill="none" stroke="#fff" stroke-width="1.4"/></symbol>
    <symbol id="ico-pin" viewBox="0 0 20 20"><circle cx="10" cy="10" r="10" fill="#f47b20"/><path d="M10 4a4 4 0 0 1 4 4c0 3-4 8-4 8s-4-5-4-8a4 4 0 0 1 4-4z" fill="#fff"/><circle cx="10" cy="8" r="1.6" fill="#f47b20"/></symbol>
    <symbol id="ico-web" viewBox="0 0 20 20"><circle cx="10" cy="10" r="7" fill="none" stroke="#f47b20" stroke-width="1.6"/><path d="M3 10h14M10 3c-3 3.5-3 10.5 0 14M10 3c3 3.5 3 10.5 0 14" fill="none" stroke="#f47b20" stroke-width="1.3"/></symbol>
  </defs>
</svg>

<section class="card front-light">
  <div class="brand-name brand-lg">KORRIM</div>
  <div class="person-name">Dana Whitlow</div>
  <div class="person-role">Machinery Sales Manager</div>
  <div class="row" style="left:28px;top:270px"><svg><use href="#ico-phone"/></svg>0400 555 012</div>
  <div class="row" style="left:28px;top:291px"><svg><use href="#ico-mail"/></svg>dana@korrim.com.au</div>
  <div class="divider"></div>
  <div class="address"><svg><use href="#ico-pin"/></svg><span>48 Harlow St<br>Ridgefield, Qld<br>4120 Australia</span></div>
  <div class="row" style="left:308px;top:266px"><svg><use href="#ico-phone"/></svg>1300 555 018</div>
  <div class="row" style="left:308px;top:291px"><svg><use href="#ico-web"/></svg>www.korrim.com.au</div>
</section>

<section class="card front-dark">
  <div class="brand-band"></div>
  <div class="brand-name brand-lg" style="top:48px">KORRIM</div>
  <div class="person-name" style="top:212px">Dana Whitlow</div>
  <div class="person-role" style="top:237px">Machinery Sales Manager</div>
  <div class="row" style="left:28px;top:264px"><svg><use href="#ico-phone"/></svg>0400 555 012</div>
  <div class="row" style="left:28px;top:285px"><svg><use href="#ico-mail"/></svg>dana@korrim.com.au</div>
  <div class="divider" style="top:194px"></div>
  <div class="address" style="top:194px"><svg><use href="#ico-pin"/></svg><span>48 Harlow St<br>Ridgefield, Qld<br>4120 Australia</span></div>
  <div class="row" style="left:308px;top:260px"><svg><use href="#ico-phone"/></svg>1300 555 018</div>
  <div class="row" style="left:308px;top:285px"><svg><use href="#ico-web"/></svg>www.korrim.com.au</div>
</section>

<section class="card back-light">
  <div class="badge" style="top:16px"></div>
  <div class="badge" style="top:126px"></div>
  <div class="badge" style="top:232px"></div>
  <ul class="service-list" style="left:127px">
    <li class="group">Pallet Containment</li><li class="item">Stretch</li><li class="item">Heat Shrink</li><li class="item">Pallet Hood</li>
    <li class="group">Flexible Packaging</li><li class="item">Bags &amp; Liners</li><li class="item">Tube</li><li class="item">Film &amp; Sheet</li><li class="item">Printed Films (12col)</li><li class="item">Shrink Films</li>
    <li class="group">Pallet Wraping</li><li class="item">Machinery</li><li class="item">Semi &amp; Fully Auto lines</li><li class="item">Finance options<br>include Lease, Rent,<br>Pay per wrap</li>
    <li class="group">General Packaging</li>
  </ul>
  <div class="brand-name brand-sm" style="left:358px">KORRIM</div>
  <div class="map-area" role="img" aria-label="Map of Australia and New Zealand with distribution location pins" style="left:340px;top:115px"></div>
  <div class="hotline" style="left:340px">1300 555 018</div>
</section>

<section class="card back-dark">
  <div class="badge" style="top:16px"></div>
  <div class="badge" style="top:126px"></div>
  <div class="badge" style="top:232px"></div>
  <div class="brand-name brand-sm" style="left:147px">KORRIM</div>
  <div class="hairline" style="top:93px"></div>
  <div class="map-area" role="img" aria-label="Map of Australia and New Zealand with distribution location pins" style="left:128px;top:112px"></div>
  <div class="hairline" style="top:275px"></div>
  <div class="hotline" style="left:130px">1300 555 018</div>
  <ul class="service-list" style="left:333px">
    <li class="group">Pallet Containment</li><li class="item">Stretch</li><li class="item">Heat Shrink</li><li class="item">Pallet Hood</li>
    <li class="group">Flexible Packaging</li><li class="item">Bags &amp; Liners</li><li class="item">Tube</li><li class="item">Film &amp; Sheet</li><li class="item">Printed Films (12col)</li><li class="item">Shrink Films</li>
    <li class="group">Pallet Wraping</li><li class="item">Machinery</li><li class="item">Semi &amp; Fully Auto lines</li><li class="item">Finance options<br>include Lease, Rent,<br>Pay per wrap</li>
    <li class="group">General Packaging</li>
  </ul>
</section>
</body>
</html>
```